Lomi-Seret - Promote and Support a community

Design a website for Ethiopean Community. the design should be friendly, easy to navigate and maintain the look & feel of the Ethiopian culture. a proposed logo is attached but it can be change according to your recommendations. This is a project we are doing at a discount rate as it supports a weak community.
Please visit their current website http://www.lomi-seret.example.il/index.php?lang=en

Target Market(s)

Community members, potential doners

Industry/Entity Type

community

Number of Pages Required

1 page

Font styles to use
Sans Serif

Requirements
Must have
• easy to navigate friendly interface

```html
<!DOCTYPE html>
<html lang="en">
<head>
<meta charset="utf-8">
<title>Lomi-Seret – Promote and Support a Community</title>
<link href="https://fonts.googleapis.com/css2?family=Montserrat:wght@300;400;500;600;700;800&display=swap" rel="stylesheet">
<style>
:root{
  --red:#e8231b;
  --dark-red:#b81a14;
  --ink:#222;
  --text:#666;
  --rule:#e52b22;
  --navy:#0b3660;
  --yellow:#ecc935;
  --orange:#e9955b;
  --mint:#12d98e;
  --footer:#0a0a0a;
}
*{margin:0;padding:0;box-sizing:border-box}
html,body{width:795px;height:1200px;overflow:hidden;background:#fff}
body{font-family:'Montserrat',sans-serif;color:var(--ink);position:relative}

.site-header{position:absolute;left:0;top:0;width:795px;height:65px;border-bottom:1px solid var(--rule);background:#fff}
.brand{position:absolute;left:116px;top:20px;display:flex;align-items:center;gap:6px}
.brand-dot{width:22px;height:22px;border-radius:50%;background:var(--red)}
.brand-name{font-size:14px;font-weight:700;color:var(--dark-red)}
.contact-icons{position:absolute;left:639px;top:16px;display:flex;gap:4px}
.contact-icons svg{width:12px;height:12px}
.main-nav{position:absolute;left:290px;top:38px;display:flex;gap:13px;font-size:8.2px;white-space:nowrap}
.main-nav a{color:#222;text-decoration:none;position:relative}
.main-nav a.active::after{content:"";position:absolute;left:9px;right:9px;bottom:-4px;height:1.5px;background:#1ea650}

.hero{position:absolute;left:0;top:66px;width:795px;height:283px;background:linear-gradient(120deg,#3b2a22 0%,#6a5243 40%,#8a7060 60%,#4a3a30 100%)}
.hero-photo{position:absolute;inset:0;background:radial-gradient(ellipse at 55% 40%,rgba(190,160,140,.45),rgba(40,28,22,.15) 70%)}
.hero-copy{position:absolute;left:131px;top:82px;color:#fff;white-space:nowrap}
.hero-kicker{font-size:27px;font-weight:700;color:var(--red);line-height:1}
.hero-line{font-size:18.5px;font-weight:300;line-height:24px;letter-spacing:.2px}
.hero-line:first-of-type{margin-top:6px}
.btn{display:flex;height:25px;font-size:7.6px;color:#fff;text-decoration:none;white-space:nowrap}
.btn-label{background:var(--red);display:flex;align-items:center;justify-content:center}
.btn-arrow{background:var(--dark-red);display:flex;align-items:center;justify-content:center;width:24px;flex:none}
.hero .btn{position:absolute;left:2px;top:89px;width:89px}
.hero .btn-label{flex:1}

.section-title{position:absolute;left:0;width:795px;text-align:center}
.section-title .lead{font-size:19px;font-weight:300;line-height:22px;letter-spacing:.5px}
.section-title .accent{font-size:19px;font-weight:800;color:var(--red);line-height:24px}
.section-title .divider{width:20px;height:4px;border-top:1px solid #555;border-bottom:1px solid #555;margin:11px auto 0}

.welcome-cols{position:absolute;left:105px;top:449px;width:586px;display:flex;justify-content:space-between}
.welcome-cols .col{width:276px}
.welcome-cols p{font-size:7.1px;line-height:13px;color:var(--text);text-align:justify;margin-bottom:13px}

.programs{position:absolute;left:107px;top:697px;display:flex;gap:15px}
.program-card{width:134px;text-align:center}
.program-photo{height:83px}
.program-card h3{font-size:9.5px;font-weight:700;line-height:11px;margin-top:9px;color:#222}
.program-card p{font-size:7.3px;line-height:12px;color:#333;margin:11px auto 0;width:120px;height:36px;overflow:hidden}
.program-go{display:flex;align-items:center;justify-content:center;width:50px;height:20px;margin:11px auto 0}
.program-go svg{width:10px;height:10px}
.view-all{position:absolute;left:348px;top:916px;width:99px;font-size:7.3px}
.view-all .btn-label{flex:1}

.supporters{position:absolute;left:112px;top:1046px;width:570px;display:flex;justify-content:space-between;align-items:center}
.supporter{background:#dfe6ef}

.site-footer{position:absolute;left:0;top:1146px;width:795px;height:54px;background:var(--footer);color:#fff;text-align:center}
.footer-nav{display:flex;justify-content:center;gap:13px;font-size:8.2px;margin-top:12px;white-space:nowrap}
.footer-nav a{color:#fff;text-decoration:none}
.copyright{font-size:7px;letter-spacing:.6px;margin-top:11px;color:#ddd}
</style>
</head>
<body>

<header class="site-header">
  <div class="brand"><span class="brand-dot"></span><span class="brand-name">Lomi-Seret</span></div>
  <div class="contact-icons">
    <svg viewBox="0 0 12 12"><circle cx="6" cy="6" r="5.4" fill="none" stroke="#222"/><path d="M4 3.3l1 1.3-.6.7c.4.9 1 1.5 1.9 1.9l.7-.6 1.3 1-.6 1c-2.4-.3-4-1.9-4.3-4.3z" fill="#222"/></svg>
    <svg viewBox="0 0 12 12"><circle cx="6" cy="6" r="5.4" fill="none" stroke="#222"/><text x="6" y="8.2" font-size="6.5" text-anchor="middle" font-family="Montserrat,sans-serif" fill="#222">@</text></svg>
    <svg viewBox="0 0 12 12"><circle cx="6" cy="6" r="5.4" fill="none" stroke="#222"/><circle cx="6" cy="6" r="3.4" fill="none" stroke="#222" stroke-width=".6"/><path d="M2.6 6h6.8M6 2.6v6.8" stroke="#222" stroke-width=".6"/><ellipse cx="6" cy="6" rx="1.5" ry="3.4" fill="none" stroke="#222" stroke-width=".6"/></svg>
  </div>
  <nav class="main-nav">
    <a class="active" href="#">Home</a><a href="#">About</a><a href="#">The Community</a><a href="#">Programs</a><a href="#">News</a><a href="#">Advocacy</a><a href="#">Partners</a><a href="#">Support Us</a>
  </nav>
</header>

<section class="hero">
  <div class="hero-photo" role="img" aria-label="Photo of many hands of different skin tones stacked together"></div>
  <div class="hero-copy">
    <div class="hero-kicker">DEDICATED</div>
    <div class="hero-line">TO IMPROVING THE HEALTH</div>
    <div class="hero-line">OF THE ETHIOPIAN ISRAELI COMMUNITY</div>
    <a class="btn" href="#"><span class="btn-label">Read More</span><span class="btn-arrow">›</span></a>
  </div>
</section>

<div class="section-title" style="top:379px">
  <div class="lead">Welcome to</div>
  <div class="accent">Lomi-Seret</div>
  <div class="divider"></div>
</div>

<div class="welcome-cols">
  <div class="col">
    <p>Aliyah (immigration) from Ethiopia to Israel and the transition to a sedentary lifestyle has resulted in the emergence of chronic diseases, in particular diabetes. While only 0.4% of the new immigrants were diagnosed with Type 2 diabetes upon arrival, by the time they had lived in Israel for ten years the figure had risen to 18% - three times as many as in the general population. The incidence of hypertension, obesity, asthma and Type 1 diabetes had also increased dramatically.</p>
    <p>Lomi-Seret was founded in 1999 by Dr. Miriam Elkayam, Head of the Endocrinology Unit at the Sharon Valley Medical Center. Her experience with Ethiopian patients made her realize that medical treatment could not succeed without culturally competent communication.</p>
  </div>
  <div class="col">
    <p>Lomi-Seret has developed into a small but dedicated NGO, delivering services throughout Israel with the backing and cooperation of a wide range of local and national bodies, including the Ministry of Health, the Ministry of Immigration, the absorption services, municipalities, the HMOs and hospitals.</p>
    <p>Today the Lomi-Seret team comprises eight Ethiopian-Israeli healthcare professionals, three Amharic-speaking medical interpreters and four health promotion specialists familiar with the Ethiopian immigrant community. Organizations within Israel and beyond now look to Lomi-Seret's programs for inspiration in their efforts to develop meaningful prevention strategies for improving the health of immigrants and minority communities.</p>
  </div>
</div>

<div class="section-title" style="top:626px">
  <div class="lead">Our</div>
  <div class="accent">Programs</div>
  <div class="divider"></div>
</div>

<div class="programs">
  <article class="program-card">
    <div class="program-photo" role="img" aria-label="Photo of community members seated at a health presentation" style="background:linear-gradient(160deg,#5a3a2a,#a08070 60%,#d8c8b8)"></div>
    <h3>Health Education<br>Presentations</h3>
    <p>To spread awareness of a health promoting lifestyle and an understanding of diabetes</p>
    <a class="program-go" href="#" style="background:var(--navy)"><svg viewBox="0 0 10 10"><path d="M1 5h8M5.5 1.5L9 5 5.5 8.5" fill="none" stroke="#fff" stroke-width="1"/></svg></a>
  </article>
  <article class="program-card">
    <div class="program-photo" role="img" aria-label="Photo of a health worker taking a blood pressure reading at a fair" style="background:linear-gradient(150deg,#9fb2c8,#d8d2cc 50%,#5aa8c4)"></div>
    <h3>Regional Health<br>Fairs</h3>
    <p>Every year, Lomi-Seret holds approximately 5 regional health fairs where members of the community meet</p>
    <a class="program-go" href="#" style="background:var(--yellow)"><svg viewBox="0 0 10 10"><path d="M1 5h8M5.5 1.5L9 5 5.5 8.5" fill="none" stroke="#fff" stroke-width="1"/></svg></a>
  </article>
  <article class="program-card">
    <div class="program-photo" role="img" aria-label="Photo of a radio host at a microphone in a studio" style="background:linear-gradient(150deg,#3a342e,#7a6e62 50%,#2c2824)"></div>
    <h3>Amharic Radio<br>Program</h3>
    <p>To reach the widest possible audience Lomi-Seret produces a fortnightly radio program on the air</p>
    <a class="program-go" href="#" style="background:var(--orange)"><svg viewBox="0 0 10 10"><path d="M1 5h8M5.5 1.5L9 5 5.5 8.5" fill="none" stroke="#fff" stroke-width="1"/></svg></a>
  </article>
  <article class="program-card">
    <div class="program-photo" role="img" aria-label="Photo of a speaker addressing a seated audience" style="background:linear-gradient(150deg,#8a7a6c,#b0a69c 50%,#6c645c)"></div>
    <h3>Health Leadership<br>Development</h3>
    <p>In partnership with Dr. Daniel Harrow of Bridges to Wellness, and Tzafon Health Services</p>
    <a class="program-go" href="#" style="background:var(--mint)"><svg viewBox="0 0 10 10"><path d="M1 5h8M5.5 1.5L9 5 5.5 8.5" fill="none" stroke="#fff" stroke-width="1"/></svg></a>
  </article>
</div>

<a class="btn view-all" href="#"><span class="btn-label">View All Programs</span><span class="btn-arrow">›</span></a>

<div class="section-title" style="top:964px">
  <div class="lead">Our</div>
  <div class="accent">Supporters</div>
  <div class="divider"></div>
</div>

<div class="supporters" aria-label="Supporter badges">
  <div class="supporter" style="width:62px;height:56px"></div>
  <div class="supporter" style="width:108px;height:32px"></div>
  <div class="supporter" style="width:68px;height:50px"></div>
  <div class="supporter" style="width:46px;height:62px"></div>
  <div class="supporter" style="width:86px;height:50px"></div>
  <div class="supporter" style="width:88px;height:34px"></div>
</div>

<footer class="site-footer">
  <nav class="footer-nav">
    <a href="#">Home</a><a href="#">About</a><a href="#">The Community</a><a href="#">Programs</a><a href="#">News</a><a href="#">Advocacy</a><a href="#">Partners</a><a href="#">Support Us</a>
  </nav>
  <div class="copyright">© 2022 Lomi-Seret. All Rights Reserved.</div>
</footer>

</body>
</html>
```